Kettle Ledger Business Card design

We need a stand out business card design for Accounting practice based in Australia specialising in pubs, clubs and hotels. We help venues maximise margins, create time and manage cashflow. One club we have been working with for the last 6 months has increased revenue by 3% and margin by 5% in this time frame. We have a back office outsourced system that costs less than having a full time employee and also allows the venues the added benefit of:<br/>-using the office space to become a revenue generating opportunity. <br/>-a complete system to enhance governance, accountability and efficiency within their operation<br/>-52 weeks cover so no hassle to cover annual/sick .. leave<br/><br/>We would like to see designs that use the colours of our logo (green & blue).
Target Market(s)
Australian Pubs, Clubs & Hotels abookkeeping, accounting and tax services
Industry/Entity Type
Accountant
Contact Information for Business Card
Miriam Oakley CPA
Principal
Accountant Tax Agent
Miriam@KettleLedger-example.com.au
0418693142
www.kettleledger-example.com.au
Accounting / Payroll / Tax / SMSF / Technology
Colors
Designer to choose colors to be used in the design.
Look and feel
Each slider illustrates characteristics of the customer's brand and the style your logo design should communicate.

```html
<!DOCTYPE html>
<html lang="en">
<head>
<meta charset="utf-8">
<title>Kettle Ledger Business Card</title>
<link rel="stylesheet" href="https://fonts.googleapis.com/css2?family=Poppins:wght@400;500;600;700&display=swap">
<style>
  :root {
    --green: #0a7a3e;
    --green-soft: #e9f3ee;
    --blue: #25389a;
    --white: #ffffff;
    --backdrop: #2a2a2e;
  }
  * { box-sizing: border-box; margin: 0; padding: 0; }
  html, body { width: 1200px; height: 800px; overflow: hidden; }
  body {
    background: var(--backdrop);
    font-family: "Poppins", sans-serif;
    position: relative;
  }
  .card {
    position: absolute;
    left: 280px;
    width: 640px;
    height: 366px;
    background: var(--white);
    overflow: hidden;
    box-shadow: 0 10px 30px rgba(0,0,0,.45);
  }
  .card--front { top: 20px; }
  .card--back { top: 414px; }

  /* Front */
  .front-decoration {
    position: absolute;
    left: 30px; top: 40px;
    width: 250px; height: 290px;
    border-radius: 50% 50% 45% 45%;
    background: var(--green-soft);
  }
  .front-brand {
    position: absolute;
    left: 0; right: 0; top: 120px;
    display: flex; align-items: center; justify-content: center; gap: 16px;
  }
  .brand-dot {
    width: 26px; height: 26px; border-radius: 50%;
    background: var(--green);
  }
  .brand-name {
    font-weight: 700;
    font-size: 52px;
    color: var(--blue);
    letter-spacing: -1px;
    line-height: 1;
  }
  .service-band {
    position: absolute;
    left: 0; right: 0; bottom: 0;
    height: 58px;
    background: var(--green);
    border-top: 5px solid var(--blue);
    display: flex; align-items: center;
    padding-left: 28px;
    color: var(--white);
    font-size: 15px;
    font-weight: 500;
    letter-spacing: .3px;
  }

  /* Back */
  .back-panel { position: absolute; inset: 0; }
  .back-decoration {
    position: absolute;
    right: 40px; top: 30px;
    width: 250px; height: 240px;
    border-radius: 50% 45% 40% 50%;
    background: linear-gradient(160deg, #ffffff 0%, #d3e9dc 100%);
    border: 6px solid var(--green);
  }
  .back-brand {
    position: absolute;
    left: 40px; top: 120px;
    display: flex; align-items: center; gap: 12px;
  }
  .back-brand .brand-name { font-size: 38px; }
  .back-brand .brand-dot { width: 20px; height: 20px; }
  .contact-block { position: absolute; left: 40px; top: 186px; }
  .person-name {
    font-weight: 700; font-size: 22px; color: var(--blue); line-height: 1.2;
  }
  .person-role {
    font-size: 14px; color: var(--green); line-height: 1.35;
  }
  .contact-list { list-style: none; margin-top: 14px; }
  .contact-item {
    display: flex; align-items: center; gap: 10px;
    font-size: 13.5px; color: var(--blue); line-height: 1;
    margin-bottom: 7px;
  }
  .contact-icon { width: 18px; height: 18px; flex: none; }
</style>
</head>
<body>

<section class="card card--front" aria-label="Business card front">
  <div class="front-decoration" role="img" aria-label="Faint large brand emblem decoration"></div>
  <div class="front-brand">
    <span class="brand-dot"></span>
    <span class="brand-name">Kettle Ledger</span>
  </div>
  <div class="service-band">Accounting | Payroll | Tax | SMSF | Technology</div>
</section>

<section class="card card--back" aria-label="Business card back">
  <svg class="back-panel" viewBox="0 0 640 366" aria-hidden="true">
    <polygon points="330,0 640,0 640,250 470,366 600,366 640,340" fill="none"/>
    <polygon points="300,95 640,0 640,250 500,366 420,366" fill="#0a7a3e" opacity="0"/>
    <path d="M330 100 L600 0 L640 0 L640 230 L560 290 Z" fill="#0a7a3e"/>
  </svg>
  <div class="back-decoration" role="img" aria-label="Large brand emblem illustration in green outline"></div>

  <div class="back-brand">
    <span class="brand-dot"></span>
    <span class="brand-name">Kettle Ledger</span>
  </div>

  <div class="contact-block">
    <p class="person-name">Miriam Oakley CPA</p>
    <p class="person-role">Principal</p>
    <p class="person-role">Accountant Tax Agent</p>
    <ul class="contact-list">
      <li class="contact-item">
        <svg class="contact-icon" viewBox="0 0 18 18" aria-hidden="true">
          <circle cx="9" cy="9" r="8.5" fill="#0a7a3e"/>
          <rect x="6" y="4" width="6" height="10" rx="1.2" fill="none" stroke="#fff" stroke-width="1.3"/>
        </svg>
        0418693142
      </li>
      <li class="contact-item">
        <svg class="contact-icon" viewBox="0 0 18 18" aria-hidden="true">
          <circle cx="9" cy="9" r="8.5" fill="#0a7a3e"/>
          <rect x="4.5" y="6" width="9" height="6.5" fill="none" stroke="#fff" stroke-width="1.2"/>
          <path d="M4.5 6 L9 10 L13.5 6" fill="none" stroke="#fff" stroke-width="1.2"/>
        </svg>
        Miriam@KettleLedger-example.com.au
      </li>
      <li class="contact-item">
        <svg class="contact-icon" viewBox="0 0 18 18" aria-hidden="true">
          <circle cx="9" cy="9" r="8.5" fill="#0a7a3e"/>
          <circle cx="9" cy="9" r="4.8" fill="none" stroke="#fff" stroke-width="1.1"/>
          <ellipse cx="9" cy="9" rx="2" ry="4.8" fill="none" stroke="#fff" stroke-width="1"/>
          <line x1="4.2" y1="9" x2="13.8" y2="9" stroke="#fff" stroke-width="1"/>
        </svg>
        www.kettleledger-example.com.au
      </li>
    </ul>
  </div>
</section>

</body>
</html>
```